Poster Design for Photography Exhibit

We are looking for a poster design for a photography exhibit featuring high-end fashion and celebrity photography.

Name of the exhibit is "MILES DORVAN: UNTITLED" (please use Helvetica Black all cap for show name.

Poster is LANDSCAPE format (2 units wide by 1 unit high).

Unfortunately due to legal reasons, we cannot use any actual Miles Dorvan photos. No can we use fashions or people on the poster!

We are looking for a high-end, sexy, bold provocative design that captures the excitement and glamour of a fashion photo shoot.

Target Market(s)

Men and Women interested in Fashion Photography and art photography in general

Industry/Entity Type

Fashion

Requirements
Must have
• landscape format, name of exhibit in Helvetica Black all caps
Nice to have
• Can be grayscale or color.
Should not have
• Logos or brand names

```html
<!DOCTYPE html>
<html lang="en">
<head>
<meta charset="utf-8">
<title>Miles Dorvan: Untitled — Exhibit Poster</title>
<link rel="stylesheet" href="https://fonts.googleapis.com/css2?family=Archivo+Black&family=Pinyon+Script&display=swap">
<style>
  :root {
    --page-bg: #ededed;
    --metal-light: #bdbdbd;
    --metal-mid: #a9a9a9;
    --metal-dark: #8e8e8e;
    --accent-yellow: #fff200;
    --band-silver: #d4d4d4;
    --ink: #0a0a0a;
    --script-white: #f4f4f4;
    --photo-warm: #e9dcc0;
    --photo-haze: #f3ede0;
    --photo-shade: #b7a78c;
  }
  * { margin: 0; padding: 0; box-sizing: border-box; }
  html, body {
    width: 1200px; height: 1000px; overflow: hidden;
    background: var(--page-bg);
  }
  .canvas { position: relative; width: 1200px; height: 1000px; }
  .poster {
    position: absolute; left: 33px; top: 210px;
    width: 1129px; height: 562px; overflow: hidden;
    background:
      linear-gradient(180deg, var(--metal-dark) 0%, var(--metal-mid) 10%, var(--metal-light) 45%, var(--metal-mid) 85%, var(--metal-dark) 100%);
  }
  .poster-bands { position: absolute; left: 0; top: 0; }
  .title {
    position: absolute; left: 47px;
    font-family: "Archivo Black", "Helvetica Neue", Arial, sans-serif;
    font-size: 62px; line-height: 1; letter-spacing: 3px;
    color: var(--ink); text-transform: uppercase;
  }
  .title-name { top: 134px; }
  .title-sub { top: 214px; left: 22px; }
  .tagline {
    position: absolute; left: 330px; top: 338px;
    font-family: "Pinyon Script", cursive;
    color: var(--script-white);
    font-size: 52px; line-height: 58px;
    text-shadow: 1px 2px 2px rgba(0,0,0,0.45);
  }
  .tagline-line { display: block; white-space: nowrap; }
  .tagline-line:first-child { padding-left: 36px; }
  .tagline-small { font-size: 30px; }
</style>
</head>
<body>
<div class="canvas">
  <section class="poster">
    <svg class="poster-bands" width="1129" height="562" viewBox="0 0 1129 562">
      <defs>
        <linearGradient id="photoTone" x1="0" y1="0" x2="1" y2="0">
          <stop offset="0" stop-color="var(--photo-shade)"/>
          <stop offset="0.35" stop-color="var(--photo-haze)"/>
          <stop offset="1" stop-color="var(--photo-warm)"/>
        </linearGradient>
      </defs>
      <polygon class="band-yellow" points="0,126 772,126 740,206 0,206" fill="var(--accent-yellow)"/>
      <polygon class="band-silver" points="0,208 457,208 420,280 0,280" fill="var(--band-silver)"/>
      <polygon class="photo-strip" role="img" aria-label="Soft-focus fashion photograph in warm hazy tones"
               points="770,126 1047,126 1012,206 738,206" fill="url(#photoTone)"/>
    </svg>
    <h1 class="title title-name">MILES DORVAN:</h1>
    <h2 class="title title-sub">UNTITLED</h2>
    <p class="tagline">
      <span class="tagline-line">High-end Fashion <span class="tagline-small">and</span></span>
      <span class="tagline-line">Celebrity Photography</span>
    </p>
  </section>
</div>
</body>
</html>
```